Book Cover

Book Title: THE QUIET LEDGER
Book Sub Title: Notes on slowing the daily rush and shaping a calmer household rhythm
Vibe: Professional, stylish, trustworthy (high-end men's fashion)
Website (for inspiration): www.brindlequarry.com
Attached: a potential photo to use for the cover, but open to other options (from our website)

```html
<!DOCTYPE html>
<html lang="en">
<head>
<meta charset="utf-8">
<title>The Quiet Ledger — Book Cover</title>
<link rel="stylesheet" href="https://fonts.googleapis.com/css2?family=Anton&family=Oswald:wght@500&display=swap">
<style>
  :root {
    --cover-paper: #edecea;
    --ink-navy: #262b42;
    --accent-red: #c43a2f;
    --photo-light: #e6e4e0;
    --photo-mid: #b9bcc4;
    --photo-deep: #3a4058;
  }
  * { margin: 0; padding: 0; box-sizing: border-box; }
  html, body {
    width: 840px;
    height: 1200px;
    overflow: hidden;
    background: var(--cover-paper);
  }
  .cover {
    position: relative;
    width: 840px;
    height: 1200px;
    background: var(--cover-paper);
  }
  .cover-title {
    position: absolute;
    left: 66px;
    top: 140px;
    width: 700px;
    height: 390px;
    overflow: visible;
  }
  .cover-title text {
    font-family: "Anton", "Oswald", sans-serif;
    fill: var(--ink-navy);
  }
  .cover-subtitle {
    position: absolute;
    left: 66px;
    top: 548px;
    font-family: "Oswald", sans-serif;
    font-weight: 500;
    font-size: 25px;
    line-height: 1.4;
    letter-spacing: 0.2px;
    text-transform: uppercase;
    color: var(--ink-navy);
  }
  .accent-rule {
    position: absolute;
    left: 636px;
    top: 566px;
    width: 130px;
    height: 4px;
    background: var(--accent-red);
  }
  .author-photo {
    position: absolute;
    left: 104px;
    top: 660px;
    width: 590px;
    height: 400px;
    background: linear-gradient(90deg, var(--photo-light) 0%, var(--photo-deep) 22%, var(--photo-light) 36%, var(--photo-mid) 60%, var(--photo-deep) 82%, var(--photo-light) 100%);
    opacity: 0.85;
  }
  .base-rule {
    position: absolute;
    left: 66px;
    top: 1102px;
    width: 134px;
    height: 4px;
    background: var(--ink-navy);
  }
</style>
</head>
<body>
  <main class="cover">
    <svg class="cover-title" viewBox="0 0 700 390" role="heading" aria-level="1" aria-label="The Quiet Ledger">
      <text x="0" y="180" font-size="195" textLength="700" lengthAdjust="spacingAndGlyphs">THE QUIET</text>
      <text x="0" y="380" font-size="195" textLength="700" lengthAdjust="spacingAndGlyphs">LEDGER</text>
    </svg>

    <p class="cover-subtitle">
      Notes on slowing the daily rush<br>
      and shaping a calmer household rhythm
    </p>
    <div class="accent-rule"></div>

    <div class="author-photo" role="img" aria-label="Photograph of the author seated on a wooden stool beside a clothing rail of jackets and shirts"></div>

    <div class="base-rule"></div>
  </main>
</body>
</html>
```